New Business Card Design Project

I would like my card design to look exactly like the logo, design, layout, and print of the current attached file. The only change I would like made would be for the print to say THE KMW GROUP instead of THE HALLORAN GROUP. Basically, just replace his group name with my group name. I would also like the backgroud to be the same texture and color as the attached file. I love the dark blue lettering and house logo on the card.

I am completely open to the rest of the card design. I just want something clean and simple. Only basic contact info required on the card. Maybe just name: Kyle M Warrick and cell # 555.914.2087 and email kyle@orchidhomesagent.com

```html
<!DOCTYPE html>
<html lang="en">
<head>
<meta charset="utf-8">
<title>The KMW Group — Business Card</title>
<link rel="stylesheet" href="https://fonts.googleapis.com/css2?family=Montserrat:wght@300;700&family=Roboto:wght@400&display=swap">
<style>
  :root {
    --navy: #141a3c;
    --card: #f2f2f0;
    --backdrop: #2b2b2d;
  }
  * { margin: 0; padding: 0; box-sizing: border-box; }
  html, body {
    width: 1200px;
    height: 1189px;
    overflow: hidden;
    background: var(--backdrop);
  }
  .sheet {
    width: 1200px;
    height: 1189px;
    display: flex;
    flex-direction: column;
    align-items: center;
    justify-content: center;
    gap: 44px;
  }
  .card {
    position: relative;
    width: 1000px;
    height: 540px;
    background: var(--card);
    border-radius: 38px;
    overflow: hidden;
    color: var(--navy);
  }
  .brand {
    display: flex;
    align-items: center;
    gap: 22px;
    font-family: "Montserrat", sans-serif;
    font-weight: 300;
    color: var(--navy);
    letter-spacing: 0.16em;
    line-height: 1.05;
    text-transform: uppercase;
  }
  .brand-square {
    width: 58px;
    height: 58px;
    background: var(--navy);
    flex: none;
  }
  .card-front .brand {
    position: absolute;
    left: 50%;
    top: 50%;
    transform: translate(-50%, -50%);
    font-size: 46px;
  }
  .card-back .brand {
    position: absolute;
    right: 70px;
    top: 80px;
    font-size: 42px;
  }
  .card-back .brand-square { width: 52px; height: 52px; }
  .rule-wide {
    position: absolute;
    left: 110px;
    right: 60px;
    top: 360px;
    height: 2px;
    background: var(--navy);
  }
  .edge-tab {
    position: absolute;
    left: 0;
    top: 420px;
    width: 20px;
    height: 58px;
    background: var(--navy);
  }
  .contact-name {
    position: absolute;
    left: 110px;
    top: 408px;
    font-family: "Montserrat", sans-serif;
    font-weight: 700;
    font-size: 34px;
  }
  .rule-name {
    position: absolute;
    left: 110px;
    top: 462px;
    width: 300px;
    height: 2px;
    background: var(--navy);
  }
  .contact-line {
    position: absolute;
    display: flex;
    align-items: center;
    gap: 12px;
    font-family: "Roboto", sans-serif;
    font-size: 28px;
    color: var(--navy);
  }
  .contact-phone { left: 110px; top: 480px; }
  .contact-email { left: 450px; top: 412px; }
  .contact-line svg { flex: none; }
</style>
</head>
<body>
  <main class="sheet">
    <section class="card card-front" aria-label="Card front">
      <div class="brand">
        <span class="brand-square" aria-hidden="true"></span>
        <span class="brand-name">The<br>KMW Group</span>
      </div>
    </section>

    <section class="card card-back" aria-label="Card back">
      <div class="brand">
        <span class="brand-square" aria-hidden="true"></span>
        <span class="brand-name">The<br>KMW Group</span>
      </div>

      <div class="rule-wide"></div>
      <div class="edge-tab"></div>

      <p class="contact-name">Kyle M Warrick</p>
      <div class="rule-name"></div>

      <p class="contact-line contact-email">
        <svg width="26" height="18" viewBox="0 0 26 18" aria-hidden="true">
          <rect x="0" y="0" width="26" height="18" fill="#141a3c"/>
          <path d="M1 1 L13 10 L25 1" fill="none" stroke="#f2f2f0" stroke-width="2"/>
        </svg>
        kyle@orchidhomesagent.com
      </p>

      <p class="contact-line contact-phone">
        <svg width="16" height="26" viewBox="0 0 16 26" aria-hidden="true">
          <rect x="1.5" y="1.5" width="13" height="23" rx="2" fill="none" stroke="#141a3c" stroke-width="2.5"/>
          <line x1="5" y1="20" x2="11" y2="20" stroke="#141a3c" stroke-width="2"/>
        </svg>
        555.914.2087
      </p>
    </section>
  </main>
</body>
</html>
```